Flyer for Merchant Capital Cash Advance business

Need Flyer Design to be advertised on Social Media Platforms and also Print it to Publish it in Magazines.
Flyer Will be printed in different sizes for different publications.
Size 1) 6.25 inches * 11 inches.
Size 2) 8 inch * 11 inch
Size 3) 8 inch * 5.5 I inch
Size 4) 5 inch * 7 inch.
Google “Merchant Capital Cash advance flyer pics” to get an idea.

Flyer Design for Merchant Cash advance business.

Merchant Cash Advance is alternate to bank loans and does not require Personal Guarantee or Collateral.
Updates

Need extra days to review

Target Market(s)

Business owners seeking loan.

Industry/Entity Type

Business Service

Font styles to use
Serif
Sans Serif
Decorative
Script

Colors

Designer to choose colors to be used in the design.

Requirements
Must have
• Content from the Files Uploaded.
• Sharp Colors.
Nice to have
• Would like to see flyer in shape of a Bank Check or a $100 Bill.
• Would like to show a Comparison between Bank Loan and MCA.
• Open to any other ideas.

```html
<!DOCTYPE html>
<html lang="en">
<head>
<meta charset="utf-8">
<title>Business Funding Made Easy – Flyer</title>
<link rel="stylesheet" href="https://fonts.googleapis.com/css2?family=Questrial&family=Allison&family=Mrs+Saint+Delafield&display=swap">
<style>
  :root {
    --pink: #c93f7c;
    --pink-deep: #a8275f;
    --pink-faint: rgba(201, 63, 124, 0.22);
    --grey-text: #6e6e6e;
    --grey-faint: rgba(110, 110, 110, 0.22);
    --paper: #ffffff;
    --stripe: #ececec;
    --bar-light: #f6f6f6;
    --bar-dark: #cfcfcf;
  }
  * { margin: 0; padding: 0; box-sizing: border-box; }
  html, body { width: 1200px; height: 900px; overflow: hidden; background: #dcdcdc; }
  .flyer {
    position: relative;
    width: 1200px; height: 900px;
    overflow: hidden;
    background:
      repeating-linear-gradient(-55deg, var(--paper) 0 5px, var(--stripe) 5px 6px);
    font-family: "Questrial", sans-serif;
  }
  .photo-panel { position: absolute; left: 0; top: 0; width: 700px; height: 900px; }

  .title-tab {
    position: absolute; left: 640px; top: 0; width: 520px; height: 190px;
    border-radius: 0 0 40px 40px;
    background: linear-gradient(180deg, #ffffff 0%, #f3f3f3 55%, #d9d9d9 100%);
    box-shadow: 0 10px 14px rgba(0,0,0,0.18);
    text-align: center;
  }
  .title-lead {
    font-family: "Mrs Saint Delafield", cursive;
    font-size: 60px; color: var(--grey-text);
    line-height: 1; padding-top: 38px;
  }
  .title-key {
    font-family: "Mrs Saint Delafield", cursive;
    font-size: 92px; color: var(--pink);
    line-height: 0.9; margin-left: 80px;
  }

  .tagline {
    position: absolute; right: 60px; top: 215px; width: 560px;
    text-align: right; color: var(--pink);
    font-size: 25px; letter-spacing: 3px; line-height: 1.35;
  }
  .tagline .emphasis { font-size: 42px; letter-spacing: 2px; }

  .backdrop-word {
    position: absolute;
    font-family: "Allison", cursive;
    line-height: 1; white-space: nowrap;
    pointer-events: none;
  }
  .word-payroll { left: 610px; top: 310px; font-size: 96px; color: var(--grey-faint); transform: rotate(-20deg); }
  .word-marketing { left: 905px; top: 315px; font-size: 50px; color: var(--grey-faint); transform: rotate(-20deg); }
  .word-advertising { left: 880px; top: 380px; font-size: 110px; color: var(--pink-faint); transform: rotate(-35deg); }
  .word-cashflow { left: 420px; top: 700px; font-size: 90px; color: var(--pink-faint); transform: rotate(-25deg); }
  .word-expansion { left: 330px; top: 800px; font-size: 60px; color: var(--pink-faint); transform: rotate(-20deg); }
  .word-inventory { left: 500px; top: 760px; font-size: 110px; color: var(--pink-faint); transform: rotate(-15deg); }

  .benefits {
    position: absolute; left: 600px; top: 415px;
    list-style: none; color: var(--pink);
    font-size: 27px; letter-spacing: 3px; line-height: 1.5;
  }
  .benefits li { display: flex; align-items: center; gap: 14px; }
  .benefits svg { width: 20px; height: 20px; flex: none; }

  .contact-fields { position: absolute; left: 620px; top: 640px; width: 580px; }
  .field { position: relative; height: 82px; }
  .field-label {
    position: absolute; right: 200px; top: 0;
    font-size: 27px; letter-spacing: 3px; color: var(--pink-deep);
  }
  .field-label .muted { color: var(--grey-text); }
  .field-bar {
    position: absolute; left: 0; right: 0; top: 38px; height: 38px;
    border-radius: 19px 0 0 19px;
    background: linear-gradient(180deg, var(--bar-light) 0%, var(--bar-dark) 100%);
    box-shadow: 0 6px 8px rgba(0,0,0,0.2);
  }
</style>
</head>
<body>
<main class="flyer">
  <svg class="photo-panel" viewBox="0 0 700 900" aria-hidden="false">
    <defs>
      <clipPath id="panel-clip"><circle cx="0" cy="300" r="560"/></clipPath>
      <linearGradient id="photo-tone" x1="0" y1="0" x2="0" y2="1">
        <stop offset="0" stop-color="#f4ede6"/>
        <stop offset="1" stop-color="#d9c3a8"/>
      </linearGradient>
    </defs>
    <circle cx="0" cy="300" r="580" fill="var(--pink)"/>
    <circle cx="0" cy="300" r="566" fill="#ffffff"/>
    <circle cx="0" cy="300" r="560" fill="#ffffff"/>
    <g clip-path="url(#panel-clip)">
      <rect x="90" y="140" width="420" height="720" fill="url(#photo-tone)"
            role="img" aria-label="Photo of a smiling woman holding a fan of hundred-dollar bills"/>
    </g>
  </svg>

  <header class="title-tab">
    <div class="title-lead">Business Funding Made</div>
    <div class="title-key">Easy</div>
  </header>

  <span class="backdrop-word word-payroll">Payroll</span>
  <span class="backdrop-word word-marketing">Marketing</span>
  <span class="backdrop-word word-advertising">Advertising</span>
  <span class="backdrop-word word-cashflow">Cash Flow</span>
  <span class="backdrop-word word-expansion">Expantion</span>
  <span class="backdrop-word word-inventory">Inventory</span>

  <p class="tagline">
    A convenient alternative<br>
    to Bank <span class="emphasis">Loan</span> Business<br>
    Capital Cash Advance
  </p>

  <ul class="benefits">
    <li><svg viewBox="0 0 20 20"><path d="M2 10 L8 16 L18 4" fill="none" stroke="currentColor" stroke-width="4"/></svg>No personal guarantee</li>
    <li><svg viewBox="0 0 20 20"><path d="M2 10 L8 16 L18 4" fill="none" stroke="currentColor" stroke-width="4"/></svg>No minimum credit score</li>
    <li><svg viewBox="0 0 20 20"><path d="M2 10 L8 16 L18 4" fill="none" stroke="currentColor" stroke-width="4"/></svg>No collateral or guarantors needed</li>
    <li><svg viewBox="0 0 20 20"><path d="M2 10 L8 16 L18 4" fill="none" stroke="currentColor" stroke-width="4"/></svg>Bankruptcy - ok</li>
    <li><svg viewBox="0 0 20 20"><path d="M2 10 L8 16 L18 4" fill="none" stroke="currentColor" stroke-width="4"/></svg>Simple one page application.</li>
  </ul>

  <section class="contact-fields">
    <div class="field"><span class="field-label">Business <span class="muted">Name</span></span><div class="field-bar"></div></div>
    <div class="field"><span class="field-label">Email <span class="muted">add</span></span><div class="field-bar"></div></div>
    <div class="field"><span class="field-label">Phone <span class="muted">Number</span></span><div class="field-bar"></div></div>
  </section>
</main>
</body>
</html>
```